Brivane Redesign

We need a face lift for our website, www.brivane.com. We sell flooring and related products nationwide. We are interested in expanding the width of the website and introducing grays and black. We want the design to be both contemporary and user friendly.

```html
<!DOCTYPE html>
<html lang="en">
<head>
<meta charset="utf-8">
<title>Brivane – Flooring</title>
<link href="https://fonts.googleapis.com/css2?family=Open+Sans:wght@400;600;700&family=Nunito:wght@300;400;700;800&family=Questrial&display=swap" rel="stylesheet">
<style>
:root{
  --bar:#5a5a5a;
  --header-top:#4a4948;
  --header-bottom:#353433;
  --section:#1e1e1e;
  --footer:#0f0f0f;
  --green:#8cc20f;
  --white:#ffffff;
  --muted:#bdbdbd;
  --soft:#9a9a9a;
  --line:#141414;
  --pill:#5b5b5b;
  --panel:#545454;
}
*{margin:0;padding:0;box-sizing:border-box}
html,body{width:1055px;height:1200px;overflow:hidden;background:var(--section)}
body{position:relative;font-family:"Open Sans",sans-serif;color:var(--white)}
a{color:inherit;text-decoration:none}
.abs{position:absolute}

.top-bar{left:0;top:0;width:1055px;height:35px;background:linear-gradient(#606060,#525252);font-size:11.5px;font-weight:600}
.top-bar nav{position:absolute;top:11px;display:flex;gap:13px}
.top-bar .left{left:100px}
.top-bar .right{right:91px}

.header{left:0;top:35px;width:1055px;height:527px;background:linear-gradient(180deg,var(--header-top),var(--header-bottom));border-bottom:2px solid var(--line)}
.brand{left:101px;top:22px;display:flex;align-items:center;gap:10px}
.brand-mark{width:20px;height:20px;background:var(--green)}
.brand-name{font-family:"Nunito",sans-serif;font-weight:800;font-size:34px;color:var(--white);letter-spacing:.5px}
.call{left:508px;top:36px;font-family:"Nunito",sans-serif;font-style:italic;font-size:17.5px;color:#d8d8d8}
.call strong{color:var(--green);font-weight:700}
.search{left:730px;top:32px;width:228px;height:28px;border-radius:14px;background:#555;display:flex;align-items:center;padding:0 12px 0 17px;justify-content:space-between;font-size:11.5px;color:#c2c2c2}
.rule{left:88px;top:86px;width:879px;height:1px;background:#222}
.categories{left:88px;top:99px;width:879px;height:30px;display:flex;align-items:center;font-family:"Nunito",sans-serif;font-weight:700;font-size:17.5px;color:#c9c9c9}
.categories a{padding:0 13px;border-left:1px solid #555;line-height:30px}
.categories a:first-child{border-left:none;padding-left:9px}
.categories .dots{display:flex;gap:5px;margin-left:8px}
.categories .dots i{width:10px;height:10px;border-radius:50%;background:var(--white);display:block}

.hero{left:88px;top:145px;width:879px;height:351px;border:4px solid #6b6b6b}
.hero-photo{position:absolute;inset:0;background:linear-gradient(160deg,#8a857c 0%,#4a453d 30%,#2b251c 55%,#1a1510 100%)}
.hero-photo::after{content:"";position:absolute;left:0;bottom:0;width:62%;height:60%;background:linear-gradient(170deg,rgba(196,142,60,.0) 0%,rgba(196,142,60,.85) 45%,rgba(140,92,30,.9) 100%)}
.hero-copy{left:498px;top:62px;width:330px}
.hero-title{font-family:"Nunito",sans-serif;font-weight:300;font-size:35px;line-height:32px}
.hero-title b{font-weight:800}
.hero-title .accent{color:var(--green);font-weight:800}
.hero-text{margin-top:14px;font-size:11.5px;font-weight:700;line-height:14px;width:325px}
.hero-arrows{left:499px;top:276px;display:flex;gap:2px}
.hero-arrows span{width:35px;height:35px;background:#0c0c0c;display:flex;align-items:center;justify-content:center}

.features{left:88px;top:590px;width:879px;display:flex;justify-content:space-between}
.feature{width:240px;text-align:center}
.feature:nth-child(1){margin-left:25px}
.feature:nth-child(3){margin-right:24px}
.feature h2{font-family:"Nunito",sans-serif;font-weight:800;font-size:35px;line-height:40px}
.feature .sub{margin-top:7px;font-family:"Questrial",sans-serif;font-size:15.5px;line-height:19px;color:var(--soft)}
.feature p{margin-top:8px;font-size:11.5px;font-weight:700;line-height:14px}
.feature .btn{display:inline-block;margin-top:16px;width:156px;height:28px;border-radius:14px;background:var(--pill);font-family:"Nunito",sans-serif;font-weight:700;font-size:15px;line-height:28px}

.divider{left:88px;top:844px;width:879px;height:1px;background:#3a3a3a}

.news-photo{left:88px;top:872px;width:293px;height:205px;background:linear-gradient(135deg,#d9d9d9 0%,#8a4a36 45%,#5b2a1c 100%)}
.news-panel{left:381px;top:872px;width:242px;height:205px;background:var(--panel);padding:28px 24px}
.news-panel h3{font-family:"Nunito",sans-serif;font-weight:800;font-size:26px}
.news-panel p{margin-top:12px;font-size:11.5px;font-weight:700;line-height:14px}
.news-panel .more{display:block;margin-top:10px;margin-left:-3px;font-family:"Questrial",sans-serif;font-size:15.5px}

.links{left:677px;top:872px;width:300px}
.link-item{position:absolute;left:0;width:300px}
.link-item svg{position:absolute;left:0;top:2px}
.link-item h4{position:absolute;left:55px;top:0;font-family:"Nunito",sans-serif;font-weight:800;font-size:21px;white-space:nowrap}
.link-item span{position:absolute;left:55px;top:30px;font-family:"Questrial",sans-serif;font-size:15.5px;line-height:18px;color:var(--soft);white-space:nowrap}

.footer{left:0;top:1106px;width:1055px;height:94px;background:var(--footer);font-size:11.5px;font-weight:600}
.footer nav{position:absolute;left:89px;display:flex;gap:16px}
.footer .row1{top:29px}
.footer .row2{top:47px}
.copyright{position:absolute;right:89px;top:47px;color:#777;font-weight:400}
</style>
</head>
<body>
<header class="top-bar abs">
  <nav class="left"><a href="#">Home</a><a href="#">About us</a><a href="#">Services</a><a href="#">Contact us</a></nav>
  <nav class="right"><a href="#">Customer Service</a><a href="#">Help</a><a href="#">Affiliates</a><a href="#">Login</a></nav>
</header>

<section class="header abs">
  <div class="brand abs"><span class="brand-mark"></span><span class="brand-name">Brivane</span></div>
  <div class="call abs">Call us on <strong>000 555 0190</strong></div>
  <div class="search abs"><span>Search here .....</span>
    <svg width="17" height="17" viewBox="0 0 17 17"><circle cx="7" cy="7" r="5.5" fill="none" stroke="#ccc" stroke-width="2"/><line x1="11" y1="11" x2="15.5" y2="15.5" stroke="#ccc" stroke-width="2.4" stroke-linecap="round"/></svg>
  </div>
  <div class="rule abs"></div>
  <nav class="categories abs">
    <a href="#">stone</a><a href="#">hardwood</a><a href="#">laminate</a><a href="#">vinyl</a><a href="#">ceramic/porcelain</a><a href="#">countertops</a><a href="#">green flooring</a><a href="#">more</a><span class="dots"><i></i><i></i></span>
  </nav>
  <div class="hero abs">
    <div class="hero-photo" role="img" aria-label="Office corridor with glass walls and polished hardwood floor"></div>
    <div class="hero-copy abs">
      <h1 class="hero-title">Pellentesque <span class="accent">vitae purus vel</span> nulla cursus <b>rutrum vitae</b></h1>
      <p class="hero-text">In libero nulla, suscipit sed purus vel, volutpat elementum risus. Morbi lacinia lectus vitae lacus feugiat elementum eu sit amet lectus. Quisque iaculis risus a sem viverra ultricies.</p>
    </div>
    <div class="hero-arrows abs">
      <span><svg width="12" height="16" viewBox="0 0 12 16"><polyline points="9,2 3,8 9,14" fill="none" stroke="#fff" stroke-width="2"/></svg></span>
      <span><svg width="12" height="16" viewBox="0 0 12 16"><polyline points="3,2 9,8 3,14" fill="none" stroke="#fff" stroke-width="2"/></svg></span>
    </div>
  </div>
</section>

<section class="features abs">
  <article class="feature"><h2>Carpet</h2><div class="sub">Pellentesque tortor<br>tellus, tempus in malesuada ut</div><p>In libero nulla, suscipit sed purus vel, volutpat elementum risus. Morbi lacinia lectus vitae lacus feugiat elementum eu sit amet lectus. Quisque iaculis risus a sem viverra ultricies.</p><a class="btn" href="#">view collections</a></article>
  <article class="feature"><h2>Laminate</h2><div class="sub">Pellentesque tortor<br>tellus, tempus in malesuada ut</div><p>In libero nulla, suscipit sed purus vel, volutpat elementum risus. Morbi lacinia lectus vitae lacus feugiat elementum eu sit amet lectus. Quisque iaculis risus a sem viverra ultricies.</p><a class="btn" href="#">view collections</a></article>
  <article class="feature"><h2>Tile</h2><div class="sub">Pellentesque tortor<br>tellus, tempus in malesuada ut</div><p>In libero nulla, suscipit sed purus vel, volutpat elementum risus. Morbi lacinia lectus vitae lacus feugiat elementum eu sit amet lectus. Quisque iaculis risus a sem viverra ultricies.</p><a class="btn" href="#">view collections</a></article>
</section>

<div class="divider abs"></div>

<div class="news-photo abs" role="img" aria-label="Hands laying reddish hardwood floor planks"></div>
<section class="news-panel abs">
  <h3>What’s new</h3>
  <p>In libero nulla, suscipit sed purus vel, volutpat elementum risus. Morbi lacinia lectus vitae lacus feugiat elementum eu sit amet lectus.</p>
  <a class="more" href="#">Click here to learn more</a>
</section>

<section class="links abs">
  <div class="link-item" style="top:0">
    <svg width="42" height="42" viewBox="0 0 42 42"><rect x="1" y="3" width="40" height="38" rx="2" fill="#6e6e6e"/><rect x="4" y="6" width="34" height="32" fill="#8a8a8a"/><polygon points="4,38 16,22 24,31 29,26 38,38" fill="#5a5a5a"/><circle cx="28" cy="14" r="3.5" fill="#5a5a5a"/></svg>
    <h4>Gallery of floors</h4><span>Pellentesque tortor<br>tellus, tempus in malesuada ut</span>
  </div>
  <div class="link-item" style="top:78px">
    <svg width="44" height="44" viewBox="0 0 44 44"><circle cx="18" cy="18" r="14" fill="none" stroke="#7a7a7a" stroke-width="3"/><line x1="28" y1="28" x2="41" y2="41" stroke="#7a7a7a" stroke-width="4" stroke-linecap="round"/></svg>
    <h4>Discover Style Quiz</h4><span>Tellus, tempus in malesuada ut</span>
  </div>
  <div class="link-item" style="top:146px">
    <svg width="42" height="44" viewBox="0 0 42 44"><path d="M6 2h28v30l-8 10H6z" fill="none" stroke="#7a7a7a" stroke-width="2.5"/><line x1="12" y1="12" x2="28" y2="12" stroke="#7a7a7a" stroke-width="2"/><line x1="12" y1="19" x2="28" y2="19" stroke="#7a7a7a" stroke-width="2"/><line x1="12" y1="26" x2="20" y2="26" stroke="#7a7a7a" stroke-width="2"/><polyline points="18,34 22,38 30,28" fill="none" stroke="#7a7a7a" stroke-width="2.5"/></svg>
    <h4>Warranty Information</h4><span>Tellus, tempus in malesuada ut</span>
  </div>
</section>

<footer class="footer abs">
  <nav class="row1"><a href="#">Customer Service</a><a href="#">About Us</a><a href="#">Privacy Policy</a><a href="#">Help</a><a href="#">Affiliates</a></nav>
  <nav class="row2"><a href="#">Site Map</a><a href="#">Search Terms</a><a href="#">Advanced Search</a><a href="#">Contact Us</a></nav>
  <div class="copyright">© 2013 brivane.com . All Rights Reserved.</div>
</footer>
</body>
</html>
```